Two Web Pages Design for an Anti-Aging Med Spa

Hi,
We are looking to redesign our website which is an Medspa in the Anti-Aging and Hormone Replacement business. We only need two pages designed. Frontpage and one inner page. and we need professional clean looks with matching colors to our logo (see attached files).
Sites we like:
http://velmorabeauty.example/
http://www.brindlequartz.example/

Target Market(s)

Mid-Age Men and Women

Industry/Entity Type

Business

Number of Pages Required

2 page

Font styles to use
Sans Serif

Colors
86cfc6
33b7a4
33a6d7
85cae6
ffffff
cadf82
9bcb3b
fde08a

Requirements
Must have
• IMPORTANT: YOU WOULD ONLY NEED TO DESIGN THE FRONTPAGE AND ONE INNER PAGE, NOT THE WHOLE SITE. FRONT-PAGE MUST INCLUDE A SLIDER. If you have any other questions please PM me.

```html
<!DOCTYPE html>
<html lang="en">
<head>
<meta charset="utf-8">
<title>Lumavie – Anti-Aging Med Spa</title>
<link rel="stylesheet" href="https://fonts.googleapis.com/css2?family=Questrial&family=Arimo:wght@400;700&display=swap">
<style>
:root{
  --lime:#9bcb3b;
  --lime-soft:#b5d95a;
  --ink:#111111;
  --text:#333333;
  --muted:#555555;
  --line:#d9d9d9;
  --band:#fafaf2;
  --dark:#2b2b2b;
  --footer:#202020;
  --white:#ffffff;
}
*{margin:0;padding:0;box-sizing:border-box}
html,body{width:872px;height:1200px;overflow:hidden;background:var(--white)}
body{position:relative;font-family:"Arimo",Arial,sans-serif;color:var(--text)}
.top-rule{position:absolute;left:0;top:0;width:872px;height:3px;background:var(--lime)}
.brand{position:absolute;left:92px;top:12px;display:flex;flex-direction:column;align-items:center;gap:5px}
.brand-dot{width:40px;height:40px;border-radius:50%;background:var(--lime)}
.brand-name{font-family:"Questrial",sans-serif;font-size:17px;color:var(--ink);letter-spacing:.5px}
.call{position:absolute;left:462px;top:14px;display:flex;align-items:center;gap:8px;font-family:"Questrial",sans-serif;font-size:12.5px;color:var(--text)}
.newsletter{position:absolute;left:626px;top:0;width:153px;height:30px;background:var(--lime);color:var(--white);font-family:"Questrial",sans-serif;font-size:15px;display:flex;align-items:center;justify-content:center;border-radius:0 0 4px 4px}
.main-nav{position:absolute;left:0;top:80px;width:872px;height:30px;border-top:2px solid #6a6a6a;border-bottom:1px solid var(--line)}
.main-nav ul{list-style:none;display:flex;position:absolute;left:90px;top:4px}
.main-nav li{font-family:"Questrial",sans-serif;font-size:9.6px;color:var(--muted);padding:4px 5.2px;height:20px;line-height:12px;white-space:nowrap}
.main-nav li.active{background:var(--lime);color:var(--white)}
.hero{position:absolute;left:0;top:110px;width:872px;height:327px;background:linear-gradient(100deg,#4a4540 0%,#8d8880 30%,#c9c6c1 55%,#d8d5d2 75%,#a8a39d 100%)}
.shop-now{position:absolute;left:378px;top:271px;width:113px;height:31px;background:var(--lime-soft);border:2px solid #e7f1c9;color:#33400f;font-family:"Questrial",sans-serif;font-size:17px;display:flex;align-items:center;justify-content:center}
.dots{position:absolute;left:413px;top:312px;display:flex;gap:7px}
.dots span{width:9px;height:9px;border-radius:50%;background:var(--white)}
.dots span.on{background:var(--ink)}
.welcome{position:absolute;left:0;top:462px;width:872px;text-align:center}
.welcome h1{font-family:"Questrial",sans-serif;font-weight:400;font-size:29px;color:var(--ink);letter-spacing:-.5px}
.welcome p{width:662px;margin:20px auto 0;font-size:10.2px;line-height:14.2px;color:var(--text)}
.welcome h1 em{font-style:normal;color:var(--lime)}
.services{position:absolute;left:0;top:614px;width:872px;height:291px;background:var(--band);display:flex;padding-left:62px}
.service{width:188px;height:240px;margin-top:24px;text-align:center;position:relative;border-right:1px dotted #cfe19a}
.service:last-child{border-right:none}
.service .photo{width:111px;height:111px;border-radius:50%;border:3px solid var(--lime-soft);margin:11px auto 0}
.service h2{font-family:"Questrial",sans-serif;font-weight:400;font-size:16.5px;color:var(--ink);margin-top:14px}
.service p{font-size:8px;line-height:11.4px;color:var(--text);width:108px;margin:4px auto 0}
.readmore{display:inline-block;margin-top:7px;width:65px;height:19px;line-height:19px;background:var(--dark);color:var(--white);font-size:8px;font-weight:700}
.readmore.on{background:var(--lime-soft)}
.testimonials{position:absolute;left:0;top:942px;width:872px;text-align:center}
.testimonials h2{font-family:"Questrial",sans-serif;font-weight:400;font-size:29px;color:var(--ink);letter-spacing:-.5px}
.avatar{width:65px;height:65px;border-radius:50%;border:3px solid var(--lime-soft);margin:24px auto 0;background:linear-gradient(135deg,#5a4035,#c9a08a)}
.testimonials p{width:640px;margin:14px auto 0;font-size:7.9px;line-height:14.2px;color:var(--text)}
.byline{margin-top:12px;font-size:9.5px;font-style:italic;color:var(--text)}
.byline span{color:var(--lime)}
.footer{position:absolute;left:0;top:1168px;width:872px;height:32px;background:var(--footer);color:#e0e0e0;font-size:8px}
.footer .copy{position:absolute;left:89px;top:12px}
.footer .links{position:absolute;right:91px;top:12px}
</style>
</head>
<body>
<div class="top-rule"></div>
<header>
  <div class="brand"><span class="brand-dot"></span><span class="brand-name">LUMAVIE</span></div>
  <div class="call">
    <svg width="10" height="16" viewBox="0 0 10 16"><rect x="0.5" y="0.5" width="9" height="15" rx="1.5" fill="#222"/><rect x="2" y="2.5" width="6" height="9" fill="#fff"/><circle cx="5" cy="13.5" r="0.9" fill="#fff"/></svg>
    <span>Call Us:&nbsp; 123 456 7890</span>
  </div>
  <div class="newsletter">Newsletter Signup</div>
  <nav class="main-nav">
    <ul>
      <li class="active">HOME</li><li>ABOUT US</li><li>HORMONE REPLACEMENT</li><li>REJUVENATION</li><li>WEIGHT AND HEALTH</li><li>BLOG</li><li>SHOP (ONLINE STORE)</li><li>TESTIMONIALS</li><li>CONTACT</li>
    </ul>
  </nav>
</header>
<section class="hero" role="img" aria-label="Slider photo of a bright treatment room with a white treatment chair, vanity and wall portrait">
  <div class="shop-now">SHOP NOW</div>
  <div class="dots"><span></span><span></span><span class="on"></span></div>
</section>
<section class="welcome">
  <h1>WELCOME TO <em>LUMA</em>VIE</h1>
  <p>You have found your ultimate one-stop beauty destination. An environment where you can escape and rejuvenate while still experiencing transformative results. We are proud to offer you the most advanced non-surgical cosmetic procedures, equipment and providers in Harborview. Lumen Medical Spa is your personal spa sanctuary from stress and worry. You will find all the rejuvenation and pampering you deserve combined with the most sophisticated cutting-edge advanced medical spa aesthetic procedures to keep you looking as great as you feel. A brilliant fusion of science and beauty which produces gorgeous results just for you.</p>
</section>
<section class="services">
  <article class="service">
    <div class="photo" role="img" aria-label="Portrait photo of a smiling mature woman" style="background:linear-gradient(135deg,#c9874a,#e9c3a0)"></div>
    <h2>BHRT for Women</h2>
    <p>Lorem Ipsum is simply dummy text of the printing and typesetting industry. Lorem Ipsum has been the industry's standard dummy text ever si</p>
    <span class="readmore on">Readmore</span>
  </article>
  <article class="service">
    <div class="photo" role="img" aria-label="Photo of a measuring tape around a waist" style="background:linear-gradient(135deg,#5c6770,#b9b2aa)"></div>
    <h2>HCG Diet</h2>
    <p>Lorem Ipsum is simply dummy text of the printing and typesetting industry. Lorem Ipsum has been the industry's standard dummy text ever si</p>
    <span class="readmore">Readmore</span>
  </article>
  <article class="service">
    <div class="photo" role="img" aria-label="Photo of fresh berries and fruit" style="background:linear-gradient(135deg,#7a2a35,#2d2f5c)"></div>
    <h2>Vitamin Bar</h2>
    <p>Lorem Ipsum is simply dummy text of the printing and typesetting industry. Lorem Ipsum has been the industry's standard dummy text ever si</p>
    <span class="readmore">Readmore</span>
  </article>
  <article class="service">
    <div class="photo" role="img" aria-label="Photo of a meal plan sheet with a pen" style="background:linear-gradient(135deg,#d9dccf,#9aa08a)"></div>
    <h2>Meal Plans</h2>
    <p>Lorem Ipsum is simply dummy text of the printing and typesetting industry. Lorem Ipsum has been the industry's standard dummy text ever si</p>
    <span class="readmore">Readmore</span>
  </article>
</section>
<section class="testimonials">
  <h2>CLIENT’S&nbsp; TESTIMONIALS</h2>
  <div class="avatar" role="img" aria-label="Client portrait photo"></div>
  <p>simply dummy text of the printing and typesetting industry. Lorem Ipsum has been the industry's standard dummy text ever since the 1500s, when an unknown printer took a galley of type and scrambled it to make a type specimen book. It has survived not only five centuries, but also the leap into electronic typesetting, remaining essentially unchanged. It was popularised in the 1960s with the release of Pressline sheets containing Lorem Ipsum passages, and more recently with desktop</p>
  <div class="byline">By <span>Admin</span></div>
</section>
<footer class="footer">
  <div class="copy">Copyright 2014 | Lumavie.example</div>
  <div class="links">Home &nbsp;|&nbsp; About Us &nbsp;|&nbsp; Hormone Replacement &nbsp;|&nbsp; Rejuvenation &nbsp;|&nbsp; Weight and Health &nbsp;|&nbsp; Blog &nbsp;|&nbsp; Shop (Online Store) &nbsp;|&nbsp; Testimonials &nbsp;|&nbsp; Contact</div>
</footer>
</body>
</html>
```